KDT Harbor Gym Team starting a weekly fitness and wellness podcast.

We need to design both a program advert poster for socials and campaigns as well as a podcast placeholder/poster.
The podcast is part of an online group training program called "Tidal Spark".
The four pillars of Tidal Spark are Fitness, Nutrition, Mindset & Community.
The program is designed and owned by KDT Harbor Gym.
The brand guidelines are similar to KDT Harbor Gym (Attached).
Target Market(s)
People aged between 30 and 60yrs old new or returning to fitness and wellness
Industry/Entity Type
Fitness
Colors
Designer to choose colors to be used in the design.
Requirements
Must have
- A strong motivational appeal. One that inspires and motivates people to take action.
Nice to have
- a captivating caption
Should not have
- Too much Zen or yoga themes.

```html
<!DOCTYPE html>
<html lang="en">
<head>
<meta charset="utf-8">
<title>Tidal Spark Podcast – Poster and Logo Sheet</title>
<link href="https://fonts.googleapis.com/css2?family=Poppins:ital,wght@0,500;0,600;0,700;1,600&family=Montserrat:wght@600;700&display=swap" rel="stylesheet">
<style>
  :root{
    --teal:#06adbd;
    --orange:#fb7a08;
    --magenta:#df3b97;
    --purple:#8a6aa8;
    --white:#ffffff;
    --ink:#000000;
    --frame:#111111;
  }
  *{margin:0;padding:0;box-sizing:border-box}
  html,body{width:778px;height:1200px;overflow:hidden;background:var(--white)}
  body{position:relative;font-family:"Poppins",sans-serif;color:var(--white)}

  .sheet-frame{position:absolute;left:0;width:778px;border:2px solid var(--frame);background:var(--white)}
  .sheet-frame--poster{top:0;height:778px}
  .sheet-frame--logos{top:797px;height:280px}
  .sheet-frame--palette{top:1096px;height:104px}

  /* Poster */
  .poster{position:absolute;left:40px;top:40px;width:697px;height:697px;overflow:hidden;
    background:linear-gradient(135deg,var(--teal) 0%,var(--purple) 32%,var(--magenta) 58%,var(--orange) 88%)}
  .brand-mark{position:absolute;display:flex;align-items:center;gap:8px}
  .brand-mark__dot{border-radius:50%;background:var(--white);flex:none}
  .brand-mark__name{font-weight:700;line-height:1.05}
  .poster .brand-mark{left:54px;top:29px}
  .poster .brand-mark__dot{width:52px;height:52px}
  .poster .brand-mark__name{font-size:17px;color:var(--white)}
  .header-rule{position:absolute;left:330px;top:53px;width:313px;height:2px;background:var(--white)}

  .poster-title{position:absolute;left:52px;top:110px;font-weight:700;font-size:72px;line-height:71px;letter-spacing:-0.5px}

  .mic-badge{position:absolute;left:487px;top:135px;width:156px;height:156px;border-radius:50%;background:var(--white)}
  .mic-badge svg{position:absolute;left:0;top:0}

  .pillars-intro{position:absolute;left:79px;top:348px;font-weight:600;font-size:15.5px}
  .pillars{position:absolute;left:55px;top:376px;width:489px;height:141px;border:2.5px solid var(--white);
    border-radius:26px;background:rgba(255,255,255,0.22)}
  .pillar{position:absolute;top:13px;width:100px;text-align:center}
  .pillar--community{left:27px}
  .pillar--fitness{left:139px}
  .pillar--nutrition{left:251px}
  .pillar--mindset{left:363px}
  .pillar__ring{width:86px;height:86px;margin:0 auto;border:2px solid var(--white);border-radius:50%;display:flex;align-items:center;justify-content:center}
  .pillar__label{display:block;margin-top:6px;font-family:"Montserrat",sans-serif;font-weight:600;font-size:13px;letter-spacing:0.2px;white-space:nowrap}

  .listen{position:absolute;left:68px;top:610px;display:flex;align-items:center;gap:12px;font-weight:600}
  .listen__lead{font-size:24px}
  .listen__channel{font-size:13px;font-weight:600}

  .presenter{position:absolute;left:502px;top:540px;width:127px;height:160px;background:var(--white);border-radius:32px 32px 0 0;
    color:var(--ink);text-align:center;padding-top:22px}
  .presenter__lead{font-style:italic;font-weight:600;font-size:12px}
  .presenter__name{margin-top:22px;font-weight:700;font-size:17px;line-height:1.15;color:var(--orange)}

  /* Logo variants */
  .logo-panel{position:absolute;display:flex;align-items:center}
  .logo-panel--orange{left:39px;top:828px;width:388px;height:218px;background:var(--orange);border:1px solid var(--frame);padding-left:62px}
  .logo-panel--dark{left:461px;top:828px;width:278px;height:102px;background:var(--ink);padding-left:36px}
  .logo-panel--light{left:461px;top:944px;width:278px;height:102px;background:var(--white);border:1px solid var(--frame);padding-left:36px}
  .logo-panel .brand-mark{position:static;gap:14px}
  .logo-panel--orange .brand-mark__dot{width:116px;height:116px}
  .logo-panel--orange .brand-mark__name{font-size:34px;color:var(--white)}
  .logo-panel--dark .brand-mark__dot,.logo-panel--light .brand-mark__dot{width:78px;height:78px}
  .logo-panel--dark .brand-mark__name{font-size:21px;color:var(--white)}
  .logo-panel--light .brand-mark__dot{border:1.5px solid var(--ink)}
  .logo-panel--light .brand-mark__name{font-size:21px;color:var(--ink)}

  /* Palette */
  .palette-label{position:absolute;top:1131px;font-family:"Montserrat",sans-serif;font-weight:700;font-size:25px;color:var(--ink);letter-spacing:0.3px}
  .palette-label--left{left:36px}
  .palette-label--right{left:477px}
  .swatch{position:absolute;top:1124px;width:47px;height:47px;border:1px solid var(--frame)}
  .swatch--teal{left:283px;background:var(--teal)}
  .swatch--orange{left:341px;background:var(--orange)}
  .swatch--magenta{left:399px;background:var(--magenta)}
</style>
</head>
<body>

<section class="sheet-frame sheet-frame--poster"></section>

<article class="poster">
  <div class="brand-mark">
    <span class="brand-mark__dot"></span>
    <span class="brand-mark__name">Tidal Spark Podcast</span>
  </div>
  <span class="header-rule"></span>

  <h1 class="poster-title">Tidal<br>Spark<br>Podcast</h1>

  <div class="mic-badge">
    <svg width="156" height="156" viewBox="0 0 156 156" aria-hidden="true">
      <defs>
        <linearGradient id="micFill" x1="0" y1="0" x2="0" y2="1">
          <stop offset="0" stop-color="#06adbd"/>
          <stop offset="0.55" stop-color="#df3b97"/>
          <stop offset="1" stop-color="#f26b3a"/>
        </linearGradient>
      </defs>
      <rect x="59" y="26" width="38" height="70" rx="19" fill="url(#micFill)"/>
      <path d="M52 78 Q55 104 78 104 Q101 104 104 78" fill="none" stroke="#f26b3a" stroke-width="5" stroke-linecap="round"/>
      <line x1="78" y1="104" x2="78" y2="126" stroke="#fb7a08" stroke-width="5"/>
      <line x1="59" y1="127" x2="97" y2="127" stroke="#fb7a08" stroke-width="5" stroke-linecap="round"/>
    </svg>
  </div>

  <p class="pillars-intro">Discover exciting and valuable programs focused on:</p>

  <div class="pillars">
    <div class="pillar pillar--community">
      <div class="pillar__ring">
        <svg width="44" height="40" viewBox="0 0 44 40" fill="#fff" aria-hidden="true">
          <circle cx="22" cy="8" r="7"/><circle cx="8" cy="12" r="5"/><circle cx="36" cy="12" r="5"/>
          <rect x="14" y="17" width="16" height="21" rx="7"/>
          <path d="M2 20h9v16Q4 36 3 28z"/><path d="M42 20h-9v16Q40 36 41 28z"/>
        </svg>
      </div>
      <span class="pillar__label">COMMUNITY</span>
    </div>
    <div class="pillar pillar--fitness">
      <div class="pillar__ring">
        <svg width="54" height="28" viewBox="0 0 54 28" fill="#fff" aria-hidden="true">
          <rect x="0" y="11" width="4" height="6"/><rect x="4" y="6" width="5" height="16"/><rect x="10" y="0" width="6" height="28"/>
          <rect x="16" y="12" width="22" height="4"/>
          <rect x="38" y="0" width="6" height="28"/><rect x="45" y="6" width="5" height="16"/><rect x="50" y="11" width="4" height="6"/>
        </svg>
      </div>
      <span class="pillar__label">FITNESS</span>
    </div>
    <div class="pillar pillar--nutrition">
      <div class="pillar__ring">
        <svg width="36" height="46" viewBox="0 0 36 46" fill="#fff" aria-hidden="true">
          <circle cx="18" cy="7" r="7"/>
          <path d="M18 46 4 32Q0 28 3 23Q8 18 13 22L18 27 23 22Q28 18 33 23Q36 28 32 32Z"/>
        </svg>
      </div>
      <span class="pillar__label">NUTRITION</span>
    </div>
    <div class="pillar pillar--mindset">
      <div class="pillar__ring">
        <svg width="38" height="42" viewBox="0 0 38 42" aria-hidden="true">
          <path fill="#fff" d="M18 2Q32 2 34 14L37 26H32V32Q32 35 29 35H25V42H7V34Q2 28 2 18Q2 2 18 2Z"/>
          <rect x="11" y="14" width="4" height="9" fill="#d86aa4"/><rect x="17" y="11" width="4" height="16" fill="#d86aa4"/><rect x="23" y="14" width="4" height="9" fill="#d86aa4"/>
        </svg>
      </div>
      <span class="pillar__label">MINDSET</span>
    </div>
  </div>

  <div class="listen">
    <span class="listen__lead">Listen Now On :</span>
    <span class="listen__channel">StreamBox</span>
    <span class="listen__channel">AudioWave</span>
  </div>

  <aside class="presenter">
    <p class="presenter__lead">Presented By:</p>
    <p class="presenter__name">KDT Harbor Gym</p>
  </aside>
</article>

<section class="sheet-frame sheet-frame--logos"></section>

<div class="logo-panel logo-panel--orange">
  <div class="brand-mark"><span class="brand-mark__dot"></span><span class="brand-mark__name">Tidal Spark<br>Podcast</span></div>
</div>
<div class="logo-panel logo-panel--dark">
  <div class="brand-mark"><span class="brand-mark__dot"></span><span class="brand-mark__name">Tidal Spark<br>Podcast</span></div>
</div>
<div class="logo-panel logo-panel--light">
  <div class="brand-mark"><span class="brand-mark__dot"></span><span class="brand-mark__name">Tidal Spark<br>Podcast</span></div>
</div>

<section class="sheet-frame sheet-frame--palette"></section>
<p class="palette-label palette-label--left">COLOR PALETTE</p>
<span class="swatch swatch--teal"></span>
<span class="swatch swatch--orange"></span>
<span class="swatch swatch--magenta"></span>
<p class="palette-label palette-label--right">FOR LOGO &amp; DESIGN</p>

</body>
</html>
```